Business Card Design for Quillmoreton Carpentry

I need a business card design for my carpentry company Quillmoreton Carpentry. Ive attached files with all information I require on both sides. Look forward to seeing your design.

```html
<!DOCTYPE html>
<html lang="en">
<head>
<meta charset="utf-8">
<title>Quillmoreton Carpentry – Business Card</title>
<link rel="stylesheet" href="https://fonts.googleapis.com/css2?family=Oswald:wght@500;700&family=Arimo:wght@400;700&display=swap">
<style>
  :root{
    --orange:#f05a28;
    --orange-soft:#f5875f;
    --peach:#fbe1d4;
    --grey:#c9c9c9;
    --ink:#222222;
    --white:#ffffff;
    --stage:#2b2b2b;
  }
  *{box-sizing:border-box;margin:0;padding:0}
  html,body{width:1200px;height:903px;overflow:hidden}
  body{background:var(--stage);position:relative;font-family:"Arimo",Arial,sans-serif}
  .card{position:absolute;width:640px;height:366px;border-radius:22px;overflow:hidden;left:280px}
  .card--back{top:60px;background:var(--orange);color:var(--white)}
  .card--front{top:477px;background:var(--white)}

  /* back */
  .back-art{position:absolute;right:0;top:0;width:330px;height:366px;
    background:radial-gradient(ellipse at 60% 55%,var(--orange-soft) 0%,rgba(245,135,95,.35) 55%,rgba(240,90,40,0) 80%)}
  .service-list{position:absolute;list-style:none;font-size:19px;line-height:30px;letter-spacing:.3px}
  .service-list li::before{content:"";display:inline-block;width:8px;height:8px;background:var(--white);margin-right:12px;vertical-align:middle}
  .service-list--left{left:42px;top:104px}
  .service-list--right{left:360px;top:36px}
  .rule{position:absolute;height:2px;background:var(--white)}
  .rule--right{left:380px;top:202px;width:220px}
  .rule--left{left:40px;top:316px;width:190px}
  .license{position:absolute;left:246px;top:300px;font-size:17px}
  .email{position:absolute;left:246px;top:326px;font-size:17px}

  /* front */
  .front-art{position:absolute;right:0;top:0;width:320px;height:366px;
    background:linear-gradient(135deg,var(--peach) 0%,#efe6e2 45%,var(--grey) 100%);opacity:.75}
  .band{position:absolute;height:4px;background:var(--orange)}
  .band--top{left:260px;top:96px;width:340px}
  .band--mid{left:40px;top:160px;width:560px}
  .band--low{left:40px;top:212px;width:560px;height:3px}
  .dot{position:absolute;width:18px;height:18px;border-radius:50%;background:var(--orange)}
  .dot--left{left:44px;top:178px}
  .dot--right{left:580px;top:118px}
  .brand-mark{position:absolute;left:250px;top:40px;width:54px;height:54px;border-radius:50%;background:var(--orange)}
  .brand-name{position:absolute;left:78px;top:102px;font-family:"Oswald",Impact,sans-serif;font-weight:700;
    font-size:60px;letter-spacing:4px;color:var(--ink);line-height:1}
  .brand-trade{position:absolute;left:250px;top:176px;font-family:"Oswald",Impact,sans-serif;font-weight:500;
    font-size:18px;letter-spacing:14px;color:var(--orange)}
  .phone{position:absolute;left:170px;top:232px;font-family:"Oswald",Impact,sans-serif;font-weight:700;
    font-size:40px;letter-spacing:1px;color:var(--ink)}
  .tagline{position:absolute;left:40px;top:296px;font-family:"Oswald",Impact,sans-serif;font-weight:700;
    font-size:23px;letter-spacing:2.5px;color:var(--orange)}
  .edge{position:absolute;left:0;bottom:0;width:100%;height:12px;background:var(--orange)}
</style>
</head>
<body>
  <section class="card card--back" aria-label="Card back">
    <div class="back-art" role="img" aria-label="Faint harbour bridge, city skyline and saw blade illustration"></div>
    <ul class="service-list service-list--right">
      <li>Shop Fitouts</li>
      <li>Refurbishments</li>
      <li>Fences/Gates</li>
      <li>Privacy Screens</li>
      <li>Cladding</li>
    </ul>
    <div class="rule rule--right"></div>
    <ul class="service-list service-list--left">
      <li>Decks and Perygolas</li>
      <li>Wall and Roof Farming</li>
      <li>Doors and Windows</li>
      <li>Attic Conversions</li>
      <li>Timber Flooring</li>
      <li>Extensions &amp; More</li>
    </ul>
    <div class="rule rule--left"></div>
    <p class="license">Lic #-418093C</p>
    <p class="email">quillmoretoncarpentry@postmail.net</p>
  </section>

  <section class="card card--front" aria-label="Card front">
    <div class="front-art" role="img" aria-label="Faint harbour bridge, city skyline and saw blade illustration"></div>
    <div class="band band--top"></div>
    <span class="dot dot--right"></span>
    <span class="brand-mark"></span>
    <h1 class="brand-name">QUILLMORETON</h1>
    <div class="band band--mid"></div>
    <span class="dot dot--left"></span>
    <p class="brand-trade">CARPENTRY</p>
    <div class="band band--low"></div>
    <p class="phone">0491570110</p>
    <p class="tagline">ANYTHINGCARPENTRY.ANYWHERE IN SYDNEY</p>
    <div class="edge"></div>
  </section>
</body>
</html>
```